Logo-Design für Alterswohnungen
Zielgruppe
Die Alterswohnungen Fennrüti AG ist eine Kapitalgesellschaft im Besitz der Gemeinde Dättlikon und erstellt für die Gemeinde einen Neubau mit Alterswohnungen und verwaltet und betreibt diese. Der Name Alterswohnungen Fennrüti AG oder die Abkürzung AWFAG wurden als Domain registriert, müssen jedoch nicht extrem hervor gestrichen werden, möglich ist auch, dass für das vermutlich 2019 fertig gestellte Objekt ein eigener Name gesucht wird. Im Moment sind wir in der Projektierungsphase und gehen davon aus, dass der Baubeginn im Frühjahr 2019 ist.
Aufgabenstellung
Es ist nicht vorgesehen, grosse Druckaufträge zu erteilen, die meisten Druckerzeugnisse werden inhouse auf den Laserdruckern erstellt. Das CD soll jedoch ansprechend sein und einfach und schnell für alle Vorlagen eingesetzt werden können.

```html
<!DOCTYPE html>
<html lang="de">
<head>
<meta charset="utf-8">
<title>Alterswohnungen Fennrüti AG – Geschäftsausstattung</title>
<link rel="stylesheet" href="https://fonts.googleapis.com/css2?family=Archivo:wght@300;400&family=Encode+Sans+Condensed:wght@300&display=swap">
<style>
  :root {
    --ink: #111114;
    --brand-grey: #a4a6b0;
    --mark-fill: #e4e5ea;
    --band: #a4a6b0;
    --paper: #ffffff;
    --edge: #d6d7dc;
    --fold: #9b6b7c;
    --bg: #ffffff;
  }
  * { box-sizing: border-box; margin: 0; padding: 0; }
  html, body { width: 1200px; height: 2600px; overflow: hidden; background: var(--bg); }
  body { position: relative; font-family: "Archivo", Arial, sans-serif; color: var(--ink); }

  .logo { position: absolute; left: 0; top: 0; width: 1200px; height: 1px; }
  .logo-text { position: absolute; text-align: right; font-weight: 300; white-space: nowrap; }
  .logo-short { display: block; color: var(--brand-grey); font-weight: 300; letter-spacing: 0.2em; margin-right: -0.2em; line-height: 1; }
  .logo-name { display: block; color: var(--ink); line-height: 1.05; letter-spacing: 0.2em; margin-right: -0.2em; }
  .logo-rule { position: absolute; width: 1px; background: var(--brand-grey); }
  .logo-mark { position: absolute; background: var(--mark-fill); }

  /* main logo */
  .logo--hero .logo-text { right: 400px; top: 6px; }
  .logo--hero .logo-short { font-size: 118px; }
  .logo--hero .logo-name { font-size: 68px; line-height: 1.15; }
  .logo--hero .logo-short + .logo-name { margin-top: 8px; }
  .logo--hero .logo-rule { left: 860px; top: 25px; height: 258px; }
  .logo--hero .logo-mark { left: 927px; top: 27px; width: 216px; height: 256px; }

  .card { position: absolute; width: 485px; height: 289px; background: var(--paper); border: 1px solid var(--edge); overflow: hidden; }
  .card--front { left: 43px; top: 403px; }
  .card--back { left: 647px; top: 403px; }

  .card--front .logo-text { right: 162px; top: 66px; }
  .card--front .logo-short { font-size: 34px; }
  .card--front .logo-name { font-size: 25px; }
  .card--front .logo-short + .logo-name { margin-top: 6px; }
  .card--front .logo-rule { left: 346px; top: 74px; height: 110px; }
  .card--front .logo-mark { left: 371px; top: 74px; width: 78px; height: 92px; }

  .card--back .logo-text { right: 124px; top: 30px; }
  .card--back .logo-short { font-size: 27px; }
  .card--back .logo-name { font-size: 19px; }
  .card--back .logo-short + .logo-name { margin-top: 3px; }
  .card--back .logo-rule { left: 377px; top: 36px; height: 88px; }
  .card--back .logo-mark { left: 394px; top: 38px; width: 60px; height: 70px; }

  .card-person { position: absolute; left: 22px; top: 148px; font-size: 15px; letter-spacing: 0.2em; }
  .card-band { position: absolute; left: 0; right: 0; bottom: 0; height: 86px; background: var(--band); color: #fff; text-align: center; font-size: 15px; letter-spacing: 0.08em; line-height: 21px; padding-top: 10px; }

  .logo--letterhead .logo-text { right: 500px; top: 815px; }
  .logo--letterhead .logo-short { font-size: 58px; color: var(--ink); }
  .logo--letterhead .logo-name { font-size: 35px; line-height: 1.1; }
  .logo--letterhead .logo-short + .logo-name { margin-top: 4px; }
  .logo--letterhead .logo-rule { left: 730px; top: 822px; height: 133px; background: var(--ink); }
  .logo--letterhead .logo-mark { left: 760px; top: 823px; width: 116px; height: 131px; }

  .letter { position: absolute; left: 40px; top: 998px; width: 1094px; height: 1560px; background: var(--paper); border: 1px solid var(--edge); }
  .letter-sender-block { position: absolute; left: 746px; top: 118px; font-size: 17px; letter-spacing: 0.12em; line-height: 21px; }
  .letter-sender-block p + p { margin-top: 10px; }
  .letter-return { position: absolute; left: 131px; top: 276px; font-size: 9.5px; letter-spacing: 0.06em; }
  .letter-return .short { color: var(--brand-grey); }
  .letter-body { position: absolute; left: 131px; font-family: "Encode Sans Condensed", "Arial Narrow", sans-serif; font-weight: 300; font-size: 17px; line-height: 28px; width: 800px; }
  .recipient { top: 312px; line-height: 23px; }
  .recipient .city { margin-top: 23px; }
  .salutation { top: 620px; }
  .para-1 { top: 678px; }
  .para-2 { top: 793px; }
  .closing { top: 1000px; }
  .signature { top: 1142px; }
  .fold-mark { position: absolute; left: 0; width: 22px; height: 1px; background: var(--fold); }
  .fold-mark--1 { top: 488px; }
  .fold-mark--2 { top: 779px; }
</style>
</head>
<body>

<div class="logo logo--hero">
  <div class="logo-text">
    <span class="logo-short">AWFAG</span>
    <span class="logo-name">Alterswohnungen</span>
    <span class="logo-name">Fennrüti AG</span>
  </div>
  <div class="logo-rule"></div>
  <div class="logo-mark" role="img" aria-label="Wappenzeichen der Gesellschaft"></div>
</div>

<div class="card card--front">
  <div class="logo-text">
    <span class="logo-short">AWFAG</span>
    <span class="logo-name">Alterswohnungen</span>
    <span class="logo-name">Fennrüti AG</span>
  </div>
  <div class="logo-rule"></div>
  <div class="logo-mark" role="img" aria-label="Wappenzeichen der Gesellschaft"></div>
</div>

<div class="card card--back">
  <div class="logo-text">
    <span class="logo-short">AWFAG</span>
    <span class="logo-name">Alterswohnungen</span>
    <span class="logo-name">Fennrüti AG</span>
  </div>
  <div class="logo-rule"></div>
  <div class="logo-mark" role="img" aria-label="Wappenzeichen der Gesellschaft"></div>
  <p class="card-person">ROLF KOBELMATT</p>
  <div class="card-band">
    <p>Musterstrasse 7 · 12345 Musterstadt</p>
    <p>T. 12 234 5678 · M. 12 234 5678 · F. 12 234 567890</p>
    <p>info@mail.com · www.internet.com</p>
  </div>
</div>

<div class="logo logo--letterhead">
  <div class="logo-text">
    <span class="logo-short">AWFAG</span>
    <span class="logo-name">Alterswohnungen</span>
    <span class="logo-name">Fennrüti AG</span>
  </div>
  <div class="logo-rule"></div>
  <div class="logo-mark" role="img" aria-label="Wappenzeichen der Gesellschaft"></div>
</div>

<div class="letter">
  <div class="letter-sender-block">
    <p>Musterstrasse 7<br>12345 Musterstadt</p>
    <p>Telefon 12 234 56<br>Telefax 12 234 567890</p>
    <p>Bank<br>IBAN CH00 001122 2233 3344 55<br>Steuer-Nr. 123/456/7890</p>
  </div>
  <p class="letter-return"><span class="short">AWFAG</span> · Musterstraße 1 · 1234 Musterstadt</p>
  <div class="letter-body recipient">
    <p>An<br>Musterfirma<br>z.Hd. Herrn Mustermann<br>Musterstrasse 7</p>
    <p class="city">12345 Musterstadt</p>
  </div>
  <div class="fold-mark fold-mark--1"></div>
  <div class="fold-mark fold-mark--2"></div>
  <p class="letter-body salutation">Sehr geehrte Danen und Herren,</p>
  <p class="letter-body para-1">Kisuaheli neuemyx doxbarcompo. Rewitz goffella quejummi vine. Esni uz blalore rindupo doan.<br>Esni uz blalore rindupo doan. Neukifa in leni dakaillien herangu de sal. Gen ounim hereo wubu,<br>ndupo Kisuaheli neuemyx doxbarcompo. Rewitz goffella quejummi vine. Esni uz.</p>
  <p class="letter-body para-2">&nbsp;Neukifa in leni dakaillien herangu de sal. Gen ounim hereo wubu, leni dakaillien herangu<br>de sal. Gen Kisuaheli neuemyx doxbarcompo. Rewitz goffella quejummi vine. Esni uz blastlore<br>inrindupo doan. Neukifa in leni dakaillien herangu de sal. Gen ounim hereo wubu, Kisuaheli<br>neuemyx doxbarcompo. Rewitz goffella quejummi vine. Rewitz goffella quejummi vine.</p>
  <p class="letter-body closing">Mit freundlichen Grüßen</p>
  <p class="letter-body signature">Rolf Kobelmatt</p>
</div>

</body>
</html>
```